タイトル  資金がなくてもはじめられる。家事や子育てと両立できる。
「好き」から始めるスクールビジネス。開業と継続経営のポイント

帯  スクールビジネス50年 手書きのチラシ・3人の生徒さんから
新たな人生が始まった。

がタイトルです。ペリカノ電子書籍
スクールビジネス50年の、現在75歳のフラワーデザイナーが歩んできた道から提案する内容です。色は少し重厚なイメージがいいかと思いますが、お任せします。
表紙デザインをお願いします。

バラが気に入りました。

沢山の提案ありがとうございました。

```html
<!DOCTYPE html>
<html lang="ja">
<head>
<meta charset="UTF-8">
<title>「好き」から始めるスクールビジネス</title>
<link href="https://fonts.googleapis.com/css2?family=Noto+Sans+JP:wght@500;700;900&family=Noto+Serif+JP:wght@700&display=swap" rel="stylesheet">
<style>
  :root {
    --wine: #9e2f45;
    --wine-dark: #8a2538;
    --ink: #1c1c1c;
    --paper: #ffffff;
    --blush: #f6c8cc;
    --edge: #d9d9d9;
    --muted: #555555;
  }
  html, body { margin: 0; padding: 0; overflow: hidden; background: var(--paper); }
  .cover {
    position: relative;
    width: 776px;
    height: 1200px;
    background: var(--paper);
    box-sizing: border-box;
    border: 2px solid var(--edge);
    font-family: "Noto Sans JP", sans-serif;
    color: var(--ink);
    overflow: hidden;
  }
  .lead {
    position: absolute;
    left: 118px;
    top: 30px;
    display: flex;
    align-items: baseline;
    white-space: nowrap;
  }
  .lead-key {
    position: relative;
    font-size: 84px;
    font-weight: 900;
    color: var(--wine);
    padding: 0 8px;
  }
  .lead-key svg { position: absolute; left: -22px; top: -6px; }
  .lead-rest { font-size: 58px; font-weight: 900; margin-left: 12px; }
  .title {
    position: absolute;
    left: 0; right: 0;
    margin: 0;
    text-align: center;
    font-weight: 900;
    color: var(--wine);
    letter-spacing: 2px;
    line-height: 1;
    font-size: 150px;
  }
  .title-1 { top: 200px; }
  .title-2 { top: 380px; }
  .subtitle {
    position: absolute;
    left: 0; right: 0;
    top: 660px;
    text-align: center;
    font-size: 40px;
    font-weight: 700;
    letter-spacing: 1px;
  }
  .points {
    position: absolute;
    left: 150px;
    top: 748px;
    font-size: 29px;
    font-weight: 700;
    line-height: 66px;
  }
  .author {
    position: absolute;
    right: 28px;
    top: 748px;
    writing-mode: vertical-rl;
    font-size: 42px;
    font-weight: 900;
    letter-spacing: 4px;
    line-height: 1;
  }
  .author-roman {
    position: absolute;
    left: 672px;
    top: 760px;
    writing-mode: vertical-rl;
    font-size: 13px;
    letter-spacing: 2px;
    color: var(--muted);
  }
  .band {
    position: absolute;
    left: 0; right: 0; bottom: 0;
    height: 240px;
    background: var(--wine-dark);
    text-align: center;
  }
  .band-head {
    margin-top: 12px;
    font-family: "Noto Serif JP", serif;
    font-size: 58px;
    font-weight: 700;
    color: var(--blush);
    line-height: 1.15;
  }
  .band-sub {
    font-size: 32px;
    font-weight: 700;
    color: var(--paper);
    line-height: 44px;
  }
  .band-box {
    margin: 8px auto 0;
    width: 640px;
    height: 84px;
    background: var(--paper);
    border-radius: 10px;
    font-size: 48px;
    font-weight: 900;
    color: var(--ink);
    line-height: 84px;
  }
</style>
</head>
<body>
  <div class="cover">
    <div class="lead">
      <span class="lead-key">
        <svg width="220" height="130" viewBox="0 0 220 130" aria-hidden="true">
          <ellipse cx="110" cy="66" rx="104" ry="58" fill="none" stroke="var(--wine)" stroke-width="4" transform="rotate(-4 110 66)"/>
        </svg>
        好き
      </span>
      <span class="lead-rest">から始める</span>
    </div>

    <h1 class="title title-1">スクール</h1>
    <div class="title title-2">ビジネス</div>

    <div class="subtitle">開業と継続経営のポイント</div>

    <div class="points">
      <div>資金がなくてもはじめられる</div>
      <div>家事や子育てと両立できる</div>
    </div>

    <div class="author">森川花代</div>
    <div class="author-roman">Hanayo Morikawa</div>

    <div class="band">
      <div class="band-head">スクールビジネス50年</div>
      <div class="band-sub">手書きのチラシ・3人の生徒さんから</div>
      <div class="band-box">新たな人生がはじまった!</div>
    </div>
  </div>
</body>
</html>
```